I need bigcommerce design template

hi, am looking for a quality, professional, attractive and mature bigcommerce template for my site. My site will sell clothes and bags and shoes. Basically what you are to do is setup the store. I have domain name which hostwren will attach them self.

```html
<!DOCTYPE html>
<html lang="en">
<head>
<meta charset="utf-8">
<title>Marco Bellamy – Store</title>
<link href="https://fonts.googleapis.com/css2?family=Open+Sans:wght@400;600;700&family=Raleway:wght@500;600&display=swap" rel="stylesheet">
<style>
  :root{
    --teal:#19c9cf;
    --teal-dark:#0bb5b9;
    --teal-light:#2fd8dc;
    --ink:#222222;
    --muted:#8a8a8a;
    --line:#dedede;
    --panel:#efefef;
    --footer:#1f1f1f;
    --footer-bottom:#2b2b2b;
    --orange:#f4a41a;
    --white:#ffffff;
  }
  *{box-sizing:border-box;margin:0;padding:0}
  html,body{width:694px;height:1200px;overflow:hidden;background:var(--white)}
  body{position:relative;font-family:'Open Sans',Arial,sans-serif;color:var(--ink)}
  a{color:inherit;text-decoration:none}

  /* header */
  .site-header{position:absolute;left:0;top:0;width:694px;height:59px;background:var(--white)}
  .brand{position:absolute;left:107px;top:20px;font-family:'Raleway',Arial,sans-serif;font-weight:600;font-size:20px;color:var(--ink);letter-spacing:.2px}
  .account-links{position:absolute;left:435px;top:9px;font-size:5.6px;color:#444;display:flex;align-items:center;gap:4px;text-transform:uppercase}
  .account-links .sep{color:#999}
  .account-links svg{margin-left:2px}
  .search{position:absolute;left:471px;top:35px;width:115px;height:14px;border:1px solid var(--line);background:#fafafa;font-size:5px;font-style:italic;color:#999;padding:4px 0 0 6px}
  .search svg{position:absolute;right:5px;top:3px}

  /* navigation */
  .main-nav{position:absolute;left:0;top:59px;width:694px;height:27px;background:linear-gradient(var(--teal-light),var(--teal-dark))}
  .main-nav ul{list-style:none;display:flex;position:absolute;left:122px;top:9px}
  .main-nav li{font-size:8.4px;color:var(--white);text-transform:uppercase;margin-right:22.6px}

  /* hero */
  .hero{position:absolute;left:0;top:86px;width:694px;height:266px;overflow:hidden}
  .hero-photo{position:absolute;inset:0;background:linear-gradient(180deg,#5a544c 0%,#7b7264 35%,#8c8476 60%,#6f6a63 100%)}
  .hero-photo::after{content:"";position:absolute;inset:0;background:radial-gradient(ellipse at 30% 70%,rgba(200,160,110,.55),transparent 45%),radial-gradient(ellipse at 75% 75%,rgba(200,160,110,.55),transparent 40%)}
  .hero-caption{position:absolute;left:201px;top:73px;width:295px;height:91px;background:rgba(255,255,255,.78);text-align:center;padding-top:13px}
  .hero-caption h1{font-family:'Raleway',Arial,sans-serif;font-weight:600;font-size:18.5px;letter-spacing:1.4px;color:var(--ink)}
  .hero-caption p{font-family:'Raleway',Arial,sans-serif;font-weight:600;font-size:10.5px;letter-spacing:1.6px;margin-top:2px}
  .hero-btn{display:inline-block;margin-top:7px;border:1px solid var(--ink);font-size:6.6px;font-weight:700;padding:4px 12px;letter-spacing:.3px}
  .hero-arrow{position:absolute;top:92px}

  /* categories */
  .categories{position:absolute;left:110px;top:376px;display:flex;gap:6px}
  .category{position:relative;width:158px;height:95px;box-shadow:0 6px 6px -3px rgba(0,0,0,.25)}
  .category-photo{position:absolute;inset:0}
  .category-label{position:absolute;left:0;right:0;bottom:0;height:27px;background:rgba(10,10,10,.85);color:var(--white);font-family:'Raleway',Arial,sans-serif;font-weight:500;font-size:11.5px;text-align:center;line-height:27px}
  .category-label.light{background:rgba(235,235,235,.88);color:var(--ink)}

  /* product sections */
  .products-section{position:absolute;left:0;width:694px}
  .new-arrivals{top:504px;height:224px;background:var(--panel);border-top:1px solid #e2e2e2}
  .best-sellers{top:728px;height:227px;background:linear-gradient(var(--teal),var(--teal-dark))}
  .section-title{position:absolute;left:0;width:694px;text-align:center;top:24px;font-family:'Raleway',Arial,sans-serif;font-weight:500;font-size:15px;letter-spacing:1.4px}
  .best-sellers .section-title{color:var(--white)}
  .product-row{position:absolute;left:109px;top:54px;display:flex;gap:5.5px}
  .product-card{width:114px;height:139px;background:var(--white);border:1px solid var(--line);position:relative;text-align:center}
  .product-photo{position:absolute;left:34px;top:8px;width:46px;height:62px;border-radius:3px}
  .product-name{position:absolute;left:0;right:0;top:79px;font-size:8.6px;color:#333}
  .product-desc{position:absolute;left:0;right:0;top:93px;font-size:5.2px;line-height:9px;color:var(--muted);white-space:nowrap}
  .product-buy{position:absolute;left:0;right:0;bottom:0;height:22px;border-top:1px solid var(--line);display:flex}
  .price{width:57px;border-right:1px solid var(--line);font-size:8.6px;font-weight:600;line-height:21px}
  .cart{flex:1;display:flex;align-items:center;justify-content:center}
  .slider-arrow{position:absolute;top:102px}

  /* features */
  .features{position:absolute;left:0;top:955px;width:694px;height:78px;background:var(--white);display:flex}
  .feature{position:relative;height:78px}
  .feature + .feature{border-left:1px solid var(--line)}
  .feature svg{position:absolute;top:24px}
  .feature h3{position:absolute;top:26px;font-size:8.6px;font-weight:600;white-space:nowrap}
  .feature p{position:absolute;top:39px;font-size:5.2px;line-height:10px;color:#444;white-space:nowrap}

  /* footer */
  .site-footer{position:absolute;left:0;top:1033px;width:694px;height:135px;background:var(--footer);color:var(--white)}
  .footer-col{position:absolute;top:27px}
  .footer-col h4{font-size:8.6px;font-weight:400;text-transform:uppercase;margin-bottom:5px}
  .footer-col li{list-style:none;font-size:6.2px;line-height:13px;color:#ddd}
  .footer-col p{font-size:6.2px;color:#ddd}
  .newsletter-form{margin-top:9px;display:flex;width:116px;height:15px}
  .newsletter-form span{flex:1;background:var(--white);color:#333;font-size:5.2px;padding:4.5px 0 0 7px}
  .newsletter-form b{width:16px;background:#333;display:flex;align-items:center;justify-content:center}
  .social{display:flex;gap:6px;margin-top:9px}
  .social i{width:10px;height:10px;border-radius:50%;background:#e6e6e6;display:block}
  .footer-bottom{position:absolute;left:0;top:1168px;width:694px;height:32px;background:var(--footer-bottom);color:#bbb;font-size:5.6px;padding:12px 0 0 116px}
</style>
</head>
<body>

<header class="site-header">
  <div class="brand">Marco Bellamy</div>
  <nav class="account-links">
    <a>Login</a><span class="sep">|</span><a>My Account</a><span class="sep">|</span><a>Sign Up</a><span class="sep">|</span><a>My Cart</a>
    <svg width="13" height="10" viewBox="0 0 13 10"><path d="M0 1h2l2 6h7l1.5-4.5H3" fill="none" stroke="#555" stroke-width="1"/><circle cx="5" cy="9" r="1" fill="#555"/><circle cx="10" cy="9" r="1" fill="#555"/></svg>
  </nav>
  <div class="search">Search here
    <svg width="8" height="8" viewBox="0 0 8 8"><circle cx="3.2" cy="3.2" r="2.4" fill="none" stroke="#999" stroke-width="1"/><path d="M5 5l2.5 2.5" stroke="#999" stroke-width="1"/></svg>
  </div>
</header>

<nav class="main-nav">
  <ul>
    <li>Home</li><li>About Us</li><li>Clothes</li><li>Shoes</li><li>Bags</li><li>Support</li><li>Shop Now</li><li>Contact</li>
  </ul>
</nav>

<section class="hero">
  <div class="hero-photo" role="img" aria-label="Close-up of a person in tan suede shoes on stone steps with glasses beside them"></div>
  <svg class="hero-arrow" style="left:86px" width="16" height="36" viewBox="0 0 16 36"><path d="M14 2L3 18l11 16" fill="none" stroke="#fff" stroke-width="2.5"/></svg>
  <svg class="hero-arrow" style="left:592px" width="16" height="36" viewBox="0 0 16 36"><path d="M2 2l11 16L2 34" fill="none" stroke="#fff" stroke-width="2.5"/></svg>
  <div class="hero-caption">
    <h1>LATEST FASHION SHOES</h1>
    <p>CRAS ANTE VITAE ENIM</p>
    <a class="hero-btn">SHOP NOW</a>
  </div>
</section>

<section class="categories">
  <div class="category">
    <div class="category-photo" role="img" aria-label="Tailored grey blazer on a mannequin" style="background:linear-gradient(135deg,#8a7055,#5a4a3c)"></div>
    <div class="category-label">FASHION CLOTHES</div>
  </div>
  <div class="category">
    <div class="category-photo" role="img" aria-label="Group of people wearing fashionable shoes" style="background:linear-gradient(135deg,#6b5b4c,#3d3a36 60%,#4f8a80)"></div>
    <div class="category-label light">LATEST SHOES</div>
  </div>
  <div class="category">
    <div class="category-photo" role="img" aria-label="Brown leather backpack with a flask outdoors" style="background:linear-gradient(135deg,#6a6a4e,#2e4d6a 55%,#8a5a35)"></div>
    <div class="category-label">BAGS</div>
  </div>
</section>

<section class="products-section new-arrivals">
  <h2 class="section-title">NEW ARRIVALS</h2>
  <svg class="slider-arrow" style="left:88px" width="12" height="30" viewBox="0 0 12 30"><path d="M11 1L1 15l10 14" fill="none" stroke="#555" stroke-width="1"/></svg>
  <svg class="slider-arrow" style="left:590px" width="12" height="30" viewBox="0 0 12 30"><path d="M1 1l10 14L1 29" fill="none" stroke="#555" stroke-width="1"/></svg>
  <div class="product-row">
    <article class="product-card">
      <div class="product-photo" role="img" aria-label="Dark brown shorts" style="background:#3b2521"></div>
      <div class="product-name">Product Name</div>
      <p class="product-desc">Ad litora torquent per conubia nostra<br>per inceptos hyme naeos Proin</p>
      <div class="product-buy"><span class="price">$25.99</span><span class="cart"><svg width="13" height="10" viewBox="0 0 13 10"><path d="M0 1h2l2 6h7l1.5-4.5H3" fill="none" stroke="#19c9cf" stroke-width="1.3"/><circle cx="5" cy="9" r="1" fill="#19c9cf"/><circle cx="10" cy="9" r="1" fill="#19c9cf"/></svg></span></div>
    </article>
    <article class="product-card">
      <div class="product-photo" role="img" aria-label="Blue long-sleeve shirt" style="background:#6f8fc9"></div>
      <div class="product-name">Product Name</div>
      <p class="product-desc">Ad litora torquent per conubia nostra<br>per inceptos hyme naeos Proin</p>
      <div class="product-buy"><span class="price">$25.99</span><span class="cart"><svg width="13" height="10" viewBox="0 0 13 10"><path d="M0 1h2l2 6h7l1.5-4.5H3" fill="none" stroke="#19c9cf" stroke-width="1.3"/><circle cx="5" cy="9" r="1" fill="#19c9cf"/><circle cx="10" cy="9" r="1" fill="#19c9cf"/></svg></span></div>
    </article>
    <article class="product-card">
      <div class="product-photo" role="img" aria-label="Red lace-up shoes" style="background:#e0403f;top:20px;height:40px"></div>
      <div class="product-name">Product Name</div>
      <p class="product-desc">Ad litora torquent per conubia nostra<br>per inceptos hyme naeos Proin</p>
      <div class="product-buy"><span class="price">$25.99</span><span class="cart"><svg width="13" height="10" viewBox="0 0 13 10"><path d="M0 1h2l2 6h7l1.5-4.5H3" fill="none" stroke="#19c9cf" stroke-width="1.3"/><circle cx="5" cy="9" r="1" fill="#19c9cf"/><circle cx="10" cy="9" r="1" fill="#19c9cf"/></svg></span></div>
    </article>
    <article class="product-card">
      <div class="product-photo" role="img" aria-label="Black leather messenger bag" style="background:#353535;top:14px;height:52px"></div>
      <div class="product-name">Product Name</div>
      <p class="product-desc">Ad litora torquent per conubia nostra<br>per inceptos hyme naeos Proin</p>
      <div class="product-buy"><span class="price">$25.99</span><span class="cart"><svg width="13" height="10" viewBox="0 0 13 10"><path d="M0 1h2l2 6h7l1.5-4.5H3" fill="none" stroke="#19c9cf" stroke-width="1.3"/><circle cx="5" cy="9" r="1" fill="#19c9cf"/><circle cx="10" cy="9" r="1" fill="#19c9cf"/></svg></span></div>
    </article>
  </div>
</section>

<section class="products-section best-sellers">
  <h2 class="section-title">BEST SELLINGS</h2>
  <svg class="slider-arrow" style="left:88px" width="12" height="30" viewBox="0 0 12 30"><path d="M11 1L1 15l10 14" fill="none" stroke="#fff" stroke-width="1"/></svg>
  <svg class="slider-arrow" style="left:590px" width="12" height="30" viewBox="0 0 12 30"><path d="M1 1l10 14L1 29" fill="none" stroke="#fff" stroke-width="1"/></svg>
  <div class="product-row">
    <article class="product-card">
      <div class="product-photo" role="img" aria-label="Brown button-up shirt" style="background:#8a7463"></div>
      <div class="product-name">Product Name</div>
      <p class="product-desc">Ad litora torquent per conubia nostra<br>per inceptos hyme naeos Proin</p>
      <div class="product-buy"><span class="price">$25.99</span><span class="cart"><svg width="13" height="10" viewBox="0 0 13 10"><path d="M0 1h2l2 6h7l1.5-4.5H3" fill="none" stroke="#19c9cf" stroke-width="1.3"/><circle cx="5" cy="9" r="1" fill="#19c9cf"/><circle cx="10" cy="9" r="1" fill="#19c9cf"/></svg></span></div>
    </article>
    <article class="product-card">
      <div class="product-photo" role="img" aria-label="Blue denim jeans" style="background:#5f86b3;left:44px;width:26px"></div>
      <div class="product-name">Product Name</div>
      <p class="product-desc">Ad litora torquent per conubia nostra<br>per inceptos hyme naeos Proin</p>
      <div class="product-buy"><span class="price">$25.99</span><span class="cart"><svg width="13" height="10" viewBox="0 0 13 10"><path d="M0 1h2l2 6h7l1.5-4.5H3" fill="none" stroke="#19c9cf" stroke-width="1.3"/><circle cx="5" cy="9" r="1" fill="#19c9cf"/><circle cx="10" cy="9" r="1" fill="#19c9cf"/></svg></span></div>
    </article>
    <article class="product-card">
      <div class="product-photo" role="img" aria-label="Beige and brown handbag" style="background:#b49a80"></div>
      <div class="product-name">Product Name</div>
      <p class="product-desc">Ad litora torquent per conubia nostra<br>per inceptos hyme naeos Proin</p>
      <div class="product-buy"><span class="price">$25.99</span><span class="cart"><svg width="13" height="10" viewBox="0 0 13 10"><path d="M0 1h2l2 6h7l1.5-4.5H3" fill="none" stroke="#19c9cf" stroke-width="1.3"/><circle cx="5" cy="9" r="1" fill="#19c9cf"/><circle cx="10" cy="9" r="1" fill="#19c9cf"/></svg></span></div>
    </article>
    <article class="product-card">
      <div class="product-photo" role="img" aria-label="Cream leather lace-up shoes" style="background:#d9cbb5"></div>
      <div class="product-name">Product Name</div>
      <p class="product-desc">Ad litora torquent per conubia nostra<br>per inceptos hyme naeos Proin</p>
      <div class="product-buy"><span class="price">$25.99</span><span class="cart"><svg width="13" height="10" viewBox="0 0 13 10"><path d="M0 1h2l2 6h7l1.5-4.5H3" fill="none" stroke="#19c9cf" stroke-width="1.3"/><circle cx="5" cy="9" r="1" fill="#19c9cf"/><circle cx="10" cy="9" r="1" fill="#19c9cf"/></svg></span></div>
    </article>
  </div>
</section>

<section class="features">
  <div class="feature" style="width:262px">
    <svg style="left:110px" width="19" height="19" viewBox="0 0 19 19"><circle cx="9.5" cy="9.5" r="9.5" fill="#f4a41a"/><path d="M5 9.8l3 3 6-6.5" fill="none" stroke="#fff" stroke-width="2"/></svg>
    <h3 style="left:136px">BEST QUALITY PRODUTS</h3>
    <p style="left:136px">Pellentesque faucibus Ut accumsan ultricies elit<br>Maecenas at justo id velit placerat</p>
  </div>
  <div class="feature" style="width:172px">
    <svg style="left:12px;top:25px" width="20" height="16" viewBox="0 0 20 16"><path d="M2 16V10Q2 5 8 5h6V1l6 6-6 6V9H9Q5 9 4 16z" fill="#f4a41a"/></svg>
    <h3 style="left:42px">FREE EASY RETURNS</h3>
    <p style="left:42px">Pellentesque faucibus Ut accumsan ultricies elit<br>Maecenas at justo id velit placerat</p>
  </div>
  <div class="feature" style="width:260px">
    <svg style="left:6px;top:27px" width="20" height="15" viewBox="0 0 20 15"><rect x="0" y="1" width="12" height="9" fill="#f4a41a"/><path d="M13 4h4l3 3v3h-7z" fill="#f4a41a"/><circle cx="4" cy="12" r="2" fill="#f4a41a"/><circle cx="16" cy="12" r="2" fill="#f4a41a"/></svg>
    <h3 style="left:34px">FREE SHIPPING</h3>
    <p style="left:34px">Pellentesque faucibus Ut accumsan ultricies elit<br>Maecenas at justo id velit place</p>
  </div>
</section>

<footer class="site-footer">
  <div class="footer-col" style="left:114px">
    <h4>Company</h4>
    <ul><li>About Us</li><li>Why Choose Us</li><li>Products</li><li>Shop Now</li></ul>
  </div>
  <div class="footer-col" style="left:225px">
    <h4>Resources</h4>
    <ul><li>Support</li><li>Help</li><li>My Account</li><li>Contact Us</li></ul>
  </div>
  <div class="footer-col" style="left:324px">
    <h4>Our Newsletter</h4>
    <p>Please sign up here for latest deals</p>
    <div class="newsletter-form"><span>Email address</span><b><svg width="5" height="7" viewBox="0 0 5 7"><path d="M1 0.5l3 3-3 3" fill="none" stroke="#fff" stroke-width="1"/></svg></b></div>
  </div>
  <div class="footer-col" style="left:476px">
    <h4>Follow Us</h4>
    <p>Please connect with us on</p>
    <div class="social"><i></i><i></i><i></i><i></i></div>
  </div>
</footer>
<div class="footer-bottom">© 2015 Company Name &nbsp;All right reserved &nbsp;Term of Use</div>

</body>
</html>
```